Re-Brand of TindelMox along with a new website design

TindelMox Ltd are a software & database development company using technologies such as PHP, C#, HTML, JQuery, Flex, AS3, MySQL, Oracle, MSSQL. We like to target all types of business from small to large.

We are great at coding but rubbish at design so thats where we need your help!

We want a complete re-brand of TindelMox including logo, website design, and business cards.

We would like a design that is clean but other than that, please feel free to be creative.

****Logo****
We are looking for a logo that appears professional but with a splash of colour that indicates a creative side. Please see below some logos that we like the look of:

We like this one because it has a nice simple and clear font for the name of the company but also an icon which is colourful and stands out. http://markvault.example/2013/03/brivelo/

We like this one because it is very clean, simple and again very clear. http://markvault.example/2013/03/quantorels/

http://markvault.example/2013/03/tide-lamp/
http://markvault.example/2013/02/velmorin/
http://markvault.example/2013/01/art-gallery-tarnwick/

As you will see from all of these examples, the font is very clear but there is always a graphic representing the company too. This is what we like.

****Website****
These are some of the examples of websites we like:
https://www.zestrune.example/
https://www.chatterlane.example/home
http://www.haldenimagery.example/
http://www.vistor.example/
http://quillbay.example/
https://www.usebriefnest.example/personal-intros
http://www.marmotpanel.example/

The current site can be found at tindelmox.example.uk

Reason: We have extended the deadline of the project by 5 days as I realise the original deadline was very tight.

Software

Requirements
Must have
• Website must have the following pages
Home
Services
Projects
About Us
Contact Us

```html
<!DOCTYPE html>
<html lang="en">
<head>
<meta charset="utf-8">
<title>TindelMox – Home</title>
<link rel="stylesheet" href="https://fonts.googleapis.com/css2?family=Open+Sans:wght@400;700&family=Oswald:wght@400;500&family=Roboto+Condensed:wght@700&family=Roboto:ital,wght@1,700;1,900&display=swap">
<style>
  :root {
    --paper: #f1f1f1;
    --white: #ffffff;
    --ink: #2b2b2b;
    --body-text: #333333;
    --orange: #f26a12;
    --orange-light: #ffa43a;
    --nav-top: #2aa8e6;
    --nav-bottom: #0a7cc4;
    --nav-divider: #0b6aa6;
    --hero-deep: #0b3f8f;
    --hero-mid: #2f78c8;
    --hero-light: #cfe3f7;
    --band-text: #1fb2ef;
    --band-edge: #0a3d6b;
    --link: #0a6fc0;
    --rule: #333333;
    --frame: #d6d6d6;
    --social: #3a7fc4;
    --arrow: #e39a12;
  }
  * { box-sizing: border-box; margin: 0; padding: 0; }
  html, body { width: 744px; height: 1200px; overflow: hidden; }
  body { background: var(--white); font-family: "Open Sans", sans-serif; color: var(--body-text); position: relative; }

  .site-header { position: absolute; left: 0; top: 0; width: 744px; height: 167px; background: var(--paper); }
  .brand { position: absolute; left: 32px; top: 76px; display: flex; align-items: center; gap: 10px; }
  .brand-dot { width: 30px; height: 30px; border-radius: 50%; background: var(--orange); }
  .brand-name { font-family: "Open Sans", sans-serif; font-weight: 700; font-size: 36px; color: var(--orange); letter-spacing: -0.5px; }
  .social { position: absolute; right: 26px; top: 79px; display: flex; gap: 8px; }
  .social span { width: 23px; height: 23px; border-radius: 50%; background: var(--social); display: block; }
  .social span:last-child { background: #d9473b; }
  .contact-phone { position: absolute; right: 26px; top: 112px; display: flex; align-items: center; gap: 8px;
    font-family: "Roboto", sans-serif; font-style: italic; font-weight: 700; font-size: 15px; color: var(--ink); letter-spacing: 0.5px; }

  .main-nav { position: absolute; left: 0; top: 167px; width: 744px; height: 33px; display: flex;
    background: linear-gradient(var(--nav-top), var(--nav-bottom)); }
  .main-nav a { flex: 1; text-align: center; line-height: 33px; font-family: "Oswald", sans-serif; font-size: 12px;
    color: var(--white); text-decoration: none; text-transform: uppercase; border-left: 1px solid var(--nav-divider); }
  .main-nav a:first-child { border-left: 0; flex: 0 0 124px; margin-left: 28px; background: linear-gradient(#ff9a2a, var(--orange)); }
  .main-nav a:nth-child(2) { flex: 0 0 136px; }

  .hero { position: absolute; left: 0; top: 200px; width: 744px; height: 313px;
    background: radial-gradient(ellipse at 55% 45%, var(--hero-light) 0%, var(--hero-mid) 35%, var(--hero-deep) 100%); }
  .hero-arrow { position: absolute; top: 144px; width: 24px; height: 24px; background: var(--arrow); }
  .hero-arrow.prev { left: 29px; } .hero-arrow.next { right: 29px; }
  .hero-arrow svg { display: block; }
  .hero-title { position: absolute; left: 37px; top: 217px; font-family: "Roboto", sans-serif; font-style: italic; font-weight: 900;
    font-size: 19px; color: var(--orange); text-transform: uppercase;
    text-shadow: -1px -1px 0 #fff, 1px -1px 0 #fff, -1px 1px 0 #fff, 1px 1px 0 #fff; }

  .cta-band { position: absolute; left: 0; top: 513px; width: 744px; height: 60px; background: #e8e8e8;
    border-top: 3px solid #9fa7b0; box-shadow: 0 4px 6px rgba(0,0,0,0.12); text-align: center; }
  .cta-band p { font-family: "Roboto", sans-serif; font-style: italic; font-weight: 900; font-size: 20px; line-height: 55px;
    color: var(--band-text); text-transform: uppercase; letter-spacing: 0.3px;
    text-shadow: -1px -1px 0 var(--band-edge), 1px -1px 0 var(--band-edge), -1px 1px 0 var(--band-edge), 1px 1px 0 var(--band-edge); }

  .service { position: absolute; left: 0; width: 744px; }
  .service-label { position: absolute; left: 28px; font-family: "Roboto Condensed", sans-serif; font-weight: 700; font-size: 16px; color: var(--ink); text-transform: uppercase; }
  .service-rule { position: absolute; left: 174px; width: 2px; height: 68px; background: var(--rule); }
  .service-title { position: absolute; left: 190px; font-family: "Roboto Condensed", sans-serif; font-weight: 700; font-size: 21px; color: var(--orange); }
  .service-copy { position: absolute; left: 30px; width: 375px; font-size: 11px; line-height: 15px; color: var(--body-text); }
  .service-copy p + p { margin-top: 15px; }
  .service-copy a { color: var(--link); text-decoration: none; }
  .service-media { position: absolute; left: 424px; width: 304px; border: 3px solid var(--white); outline: 1px solid var(--frame);
    box-shadow: 0 0 4px rgba(0,0,0,0.2); padding: 4px; background: var(--white); }
  .service-media div { width: 100%; height: 100%; }

  .web-design { top: 615px; }
  .rich-apps { top: 839px; }
</style>
</head>
<body>
  <header class="site-header">
    <div class="brand"><span class="brand-dot"></span><span class="brand-name">TindelMox</span></div>
    <div class="social" aria-label="Social links"><span></span><span></span><span></span></div>
    <div class="contact-phone">
      <svg width="22" height="26" viewBox="0 0 22 26" aria-hidden="true">
        <circle cx="11" cy="6" r="5" fill="#1aa3e0"/>
        <path d="M2 24c0-7 4-11 9-11s9 4 9 11z" fill="#1aa3e0"/>
        <circle cx="11" cy="19" r="3" fill="#fff"/>
      </svg>
      <span>555 0142 7731</span>
    </div>
  </header>

  <nav class="main-nav">
    <a href="#">Home</a><a href="#">Services</a><a href="#">Projects</a><a href="#">About Us</a><a href="#">Contact Us</a>
  </nav>

  <section class="hero" role="img" aria-label="Tablet displaying a world map beside a blue globe with streams of binary digits">
    <span class="hero-arrow prev"><svg width="24" height="24" viewBox="0 0 24 24"><path d="M14 7l-5 5 5 5" stroke="#fff" stroke-width="2" fill="none"/></svg></span>
    <span class="hero-arrow next"><svg width="24" height="24" viewBox="0 0 24 24"><path d="M10 7l5 5-5 5" stroke="#fff" stroke-width="2" fill="none"/></svg></span>
    <h1 class="hero-title">Lorel ipsum dlors it amet</h1>
  </section>

  <div class="cta-band"><p>For beter performance and flawless job contact us</p></div>

  <section class="service web-design">
    <h2 class="service-label" style="top:22px">What we do</h2>
    <span class="service-rule" style="top:0"></span>
    <h3 class="service-title" style="top:16px">Website Design</h3>
    <div class="service-copy" style="top:92px">
      <p>Your website is a representation of who you are or what your business stands for. If you feel your website could better show off who you are and what you do TindelMox is the right team for you. You will work with a team that will find out exactly what you want, deliver quickly and not break the bank. Our team would be happy to talk over your ideas at a time and venue that is convenient for you so get in touch by <a href="#">clicking here</a>.</p>
    </div>
    <figure class="service-media" style="top:70px;height:123px">
      <div role="img" aria-label="Hands typing on a laptop keyboard" style="background:linear-gradient(135deg,#1c2c44 0%,#6c88a8 40%,#e6eef6 75%,#c9d3dd 100%)"></div>
    </figure>
  </section>

  <section class="service rich-apps">
    <h2 class="service-label" style="top:22px">What we do</h2>
    <span class="service-rule" style="top:0"></span>
    <h3 class="service-title" style="top:16px">Rich Internet Applications</h3>
    <div class="service-copy" style="top:91px">
      <p>You may be asking yourself, “what the heck is a Rich Internet Application..?” The chances are you play with one every day. If you have ever used Stackwrite Docs then you know what we are talking about.</p>
      <p>A Rich Internet Application is all about offering your clients a more engaging and immersive experience and in turn, you will receive greater customer loyalty and efficiency.</p>
      <p>Whether you want to show real-time information, rich media content or data visualisations TindelMox have the expertise to put your web application ideas into overdrive.</p>
      <p>If this is something you would like to talk about, our team is always here to help. <a href="#">Click here</a> and get in contact.</p>
    </div>
    <figure class="service-media" style="top:70px;height:246px">
      <div role="img" aria-label="Green digital grid with flowing data waves and the words social media" style="background:radial-gradient(ellipse at 50% 40%,#6fd35a 0%,#1e8a2a 45%,#08320e 100%)"></div>
    </figure>
  </section>
</body>
</html>
```